Web design for Money Service Business (uncoded)

We need a very basic website with 5-6 pages. Home page, Services, Transfer(How to use our service), About us, Contact us, FAQ
Our company name is Meridale Exchange. We are a company that deals with currency exchange and international money transfer. We do cash exchange and international money transfers to bank accounts all over the world. We offer highly competitive exchange rates so usually attract customers who transfer money over $10,000. Our niche is with larger sums of money, the design needs to be professional and communicate trust, security and stability.

```html
<!DOCTYPE html>
<html lang="en">
<head>
<meta charset="utf-8">
<title>Meridale Exchange — Cash Exchange &amp; International Money Transfer</title>
<link href="https://fonts.googleapis.com/css2?family=Ubuntu:wght@300;400;500;700&display=swap" rel="stylesheet">
<style>
:root{
  --navy:#1d4a78;
  --blue:#2a6aa3;
  --nav:#2f6ea8;
  --nav-dark:#245c8f;
  --hero-top:#1d4c7a;
  --hero-mid:#2c6699;
  --orange:#f39a1f;
  --orange-dark:#e0800c;
  --text:#444;
  --muted:#777;
  --card:#f3f3f3;
  --page:#ececec;
  --white:#fff;
}
*{box-sizing:border-box;margin:0;padding:0}
html,body{width:1200px;height:806px;overflow:hidden}
body{font-family:"Ubuntu",sans-serif;background:var(--page);color:var(--text);position:relative}
.wrap{width:806px;margin:0 auto;position:relative}

.site-header{height:85px;background:var(--white)}
.site-header .wrap{height:85px;display:flex;justify-content:space-between;align-items:center}
.brand{display:flex;align-items:center;gap:10px;font-size:30px;font-weight:500;color:var(--navy);letter-spacing:.3px}
.brand-dot{width:26px;height:26px;border-radius:50%;background:var(--orange)}
.hotlines{display:flex;gap:19px;margin-right:3px}
.hotline span{display:block;font-size:11px;color:var(--muted)}
.hotline strong{display:block;font-size:16px;font-weight:400;color:#444;margin-top:3px}

.main-nav{height:43px;background:linear-gradient(var(--nav),var(--nav-dark))}
.main-nav .wrap{height:43px;display:flex;align-items:center}
.main-nav ul{list-style:none;display:flex;height:43px}
.main-nav li a{display:flex;height:43px;align-items:center;justify-content:center;color:var(--white);text-decoration:none;font-size:12px;font-weight:500;text-transform:uppercase}
.main-nav li:nth-child(1) a{width:86px;background:#245785}
.main-nav li:nth-child(2) a{width:103px;margin-left:2px}
.main-nav li:nth-child(3) a{width:104px}
.main-nav li:nth-child(4) a{width:102px}
.main-nav li:nth-child(5) a{width:100px}
.main-nav li:nth-child(6) a{width:76px}
.btn-account{position:absolute;right:-3px;top:5px;width:127px;height:31px;border-radius:3px;background:linear-gradient(#f7aa38,var(--orange-dark));color:var(--white);font-size:12.5px;font-weight:500;display:flex;align-items:center;justify-content:center;box-shadow:0 1px 2px rgba(0,0,0,.3)}

.hero{height:351px;position:relative;background:radial-gradient(ellipse at 50% 40%,var(--hero-mid),var(--hero-top) 75%);overflow:hidden}
.skyline{position:absolute;left:0;right:0;bottom:0;height:180px;background:linear-gradient(rgba(60,110,160,0),rgba(58,108,156,.55))}
.hero .wrap{height:351px}
.hero-title{position:absolute;top:70px;left:0;font-size:26px;font-weight:300;line-height:33px;color:var(--white);letter-spacing:.3px}
.hero-title b{font-weight:700}
.hero-actions{position:absolute;top:216px;left:1px;display:flex;gap:17px}
.hero-actions a{width:164px;height:43px;border-radius:3px;display:flex;align-items:center;justify-content:center;color:var(--white);font-size:18px;font-weight:500;text-decoration:none;box-shadow:0 2px 3px rgba(0,0,0,.35)}
.btn-cash{background:linear-gradient(#f7aa38,var(--orange-dark))}
.btn-transfer{background:linear-gradient(#3a7ab5,#25609a);border:1px solid #4580b8}
.rate-box{position:absolute;right:0;top:69px;width:240px;height:189px;background:rgba(22,60,100,.55);text-align:center;color:var(--white)}
.rate-box h2{font-size:16px;font-weight:400;margin-top:23px}
.rate-value{display:flex;justify-content:center;align-items:center;margin-top:16px}
.rate-value strong{font-size:48px;font-weight:700;padding-right:15px;border-right:1px solid rgba(255,255,255,.6);line-height:38px;margin-left:7px}
.rate-value span{font-size:15px;text-align:left;padding-left:15px;line-height:20px}
.rate-box p{font-size:10.5px;margin-top:28px;padding-left:6px}

.panels{background:var(--white);height:181px;padding:19px 19px 0 20px;display:flex;gap:21px}
.panel{background:var(--card);height:140px;border-radius:2px;padding:15px 15px 0 15px}
.panel:nth-child(1){width:237px}
.panel:nth-child(2){width:237px}
.panel:nth-child(3){width:251px}
.panel h3{font-size:15.5px;font-weight:500;color:#333;display:flex;justify-content:space-between;align-items:center}
.panel p{font-size:10.5px;line-height:12.5px;color:var(--muted);margin-top:8px;padding-left:2px;height:54px}
.panel a{display:block;font-size:11.5px;color:var(--orange);text-decoration:none;margin-top:9px;padding-left:2px}
.arrows{display:flex;gap:7px;margin-right:14px}

.site-footer{text-align:center;font-size:10.5px;color:var(--muted)}
.footer-note{padding-top:31px;padding-bottom:19px;border-bottom:1px solid #dadada}
.footer-links{list-style:none;display:flex;justify-content:center;margin-top:15px}
.footer-links li{padding:0 15px;border-left:1px solid #ccc;line-height:11px}
.footer-links li:first-child{border-left:none}
.footer-links li:first-child a{color:var(--orange)}
.footer-links a{color:var(--muted);text-decoration:none}
.copyright{margin-top:10px}
</style>
</head>
<body>
<header class="site-header">
  <div class="wrap">
    <div class="brand"><span class="brand-dot"></span>Meridale Exchange</div>
    <div class="hotlines">
      <div class="hotline"><span>Money Transfer</span><strong>080 4417 2650</strong></div>
      <div class="hotline"><span>ForeignExchange</span><strong>080 4417 2650</strong></div>
    </div>
  </div>
</header>

<nav class="main-nav">
  <div class="wrap">
    <ul>
      <li><a href="#">Home</a></li>
      <li><a href="#">Services</a></li>
      <li><a href="#">Transfer</a></li>
      <li><a href="#">About Us</a></li>
      <li><a href="#">Contact Us</a></li>
      <li><a href="#">FAQ</a></li>
    </ul>
    <a class="btn-account" href="#" style="text-decoration:none">Open An Account</a>
  </div>
</nav>

<section class="hero">
  <div class="skyline" role="img" aria-label="Faint city skyline silhouette"></div>
  <div class="wrap">
    <h1 class="hero-title">We Do Cash <b>Exchange</b> and International<br><b>Money Transfers</b> to Bank Accounts<br>All Over The World</h1>
    <div class="hero-actions">
      <a class="btn-cash" href="#">Cash Exchange</a>
      <a class="btn-transfer" href="#">Money Transfer</a>
    </div>
    <aside class="rate-box">
      <h2>The Rate Today</h2>
      <div class="rate-value"><strong>3.65</strong><span>USD<br>GBP</span></div>
      <p>The rate could change throught the day</p>
    </aside>
  </div>
</section>

<main class="wrap">
  <section class="panels">
    <article class="panel">
      <h3>About Meridale Exchange</h3>
      <p>Lorem ipsum dolor sit amet, consectetuer adipiscing elit, sed diam nonummy nibh euitincidunt ut laoreet dolore magna aliqua mvolutpat.</p>
      <a href="#">Read More</a>
    </article>
    <article class="panel">
      <h3>Discount</h3>
      <p>Ut wisi enim ad minim veniam, quis nostrud exerci tation ullamcorper suscipit lobortis nisl ut aliquip ex ea commodo consequat.</p>
      <a href="#">Get Discount</a>
    </article>
    <article class="panel">
      <h3>News
        <span class="arrows">
          <svg width="7" height="10" viewBox="0 0 7 10"><path d="M7 0v10L0 5z" fill="#ccc"/></svg>
          <svg width="7" height="10" viewBox="0 0 7 10"><path d="M0 0v10l7-5z" fill="#888"/></svg>
        </span>
      </h3>
      <p>Lorem ipsum dolor sit amet, consectetuer adipiscing elit, sed diam nonummy nibh eui tincidunt ut laoreet dolore magna aliquam volutpat.</p>
      <a href="#">View all</a>
    </article>
  </section>

  <footer class="site-footer">
    <p class="footer-note">Nam liber tempor cum soluta nobis eleifend option congue nihil imperdiet doming id quod mazim placerat facer possim assum.</p>
    <ul class="footer-links">
      <li><a href="#">Customer Agreement</a></li>
      <li><a href="#">Privacy Policy</a></li>
      <li><a href="#">Risk Warning</a></li>
      <li><a href="#">FAQ</a></li>
      <li><a href="#">Contact Us</a></li>
    </ul>
    <p class="copyright">© 2013 meridaleexchange.com.&nbsp; All right reserved.</p>
  </footer>
</main>
</body>
</html>
```